Design professional, clean and neat beauty clinic

design an instagram style flyer similar style but have my own branding. Like they have their own. Must look different but also similar/better in professionalism. source file also needed.

Font styles to use
Sans Serif

```html
<!DOCTYPE html>
<html lang="en">
<head>
<meta charset="utf-8">
<title>Beauty Therapy Course Flyer</title>
<link rel="stylesheet" href="https://fonts.googleapis.com/css2?family=Raleway:ital,wght@0,300;0,400;0,500;0,600;1,300;1,400;1,800&display=swap">
<style>
  :root {
    --paper: #ffffff;
    --gold: #d6b278;
    --cream: #f3ebd8;
    --plum: #584a55;
    --mist: #e6e9f0;
    --ink: #3b3a3d;
    --ink-plum: #4a3f48;
    --skin-warm: #ecd3c6;
    --skin-soft: #f4e6de;
    --hair-tone: #8c7b74;
  }
  html, body {
    margin: 0;
    padding: 0;
    width: 1199px;
    height: 1200px;
    overflow: hidden;
    background: var(--paper);
  }
  .flyer {
    display: block;
    width: 1199px;
    height: 1200px;
    font-family: "Raleway", sans-serif;
  }
  .logo-name { font-size: 84px; font-weight: 400; font-style: italic; fill: var(--ink); }
  .tagline { font-size: 39px; font-weight: 600; fill: var(--ink-plum); }
  .intro { font-size: 37px; font-weight: 300; fill: var(--ink); }
  .headline { font-size: 82px; font-weight: 400; fill: var(--ink); }
  .subhead { font-size: 33px; font-weight: 800; font-style: italic; fill: var(--ink); }
  .booking { font-size: 44px; font-weight: 300; font-style: italic; fill: var(--paper); }
  .info-label { font-size: 36px; font-weight: 300; font-style: italic; fill: var(--ink); }
  .phone { font-size: 53px; font-weight: 400; font-style: italic; fill: var(--ink); }
  .email { font-size: 33px; font-weight: 300; font-style: italic; fill: var(--ink); }
</style>
</head>
<body>
<svg class="flyer" viewBox="0 0 1199 1200" xmlns="http://www.w3.org/2000/svg">
  <defs>
    <radialGradient id="photoTone" cx="560" cy="560" r="430" gradientUnits="userSpaceOnUse">
      <stop offset="0" stop-color="var(--skin-warm)"/>
      <stop offset="0.45" stop-color="var(--skin-soft)"/>
      <stop offset="1" stop-color="var(--paper)"/>
    </radialGradient>
    <radialGradient id="hairTone" cx="690" cy="330" r="260" gradientUnits="userSpaceOnUse">
      <stop offset="0" stop-color="var(--hair-tone)" stop-opacity="0.35"/>
      <stop offset="1" stop-color="var(--hair-tone)" stop-opacity="0"/>
    </radialGradient>
  </defs>

  <rect class="background" width="1199" height="1200" fill="var(--paper)"/>

  <!-- treatment photograph area -->
  <g class="hero-photo" role="img"
     aria-label="Photo: gloved hands giving a cosmetic injection to a woman's temple">
    <polygon points="0,190 940,190 940,804 241,804 102,680 0,585" fill="url(#photoTone)"/>
    <polygon points="0,190 940,190 940,804 241,804 102,680 0,585" fill="url(#hairTone)"/>
  </g>

  <!-- top-right tag panel -->
  <polygon class="accent-sliver" points="716,114 738,95 761,114" fill="var(--mist)"/>
  <polygon class="accent-sliver" points="785,162 800,149 820,162" fill="var(--mist)"/>
  <polygon class="tag-panel" points="827,0 1199,0 1199,442 1166,499 738,87" fill="var(--cream)"/>

  <g class="tagline-group" transform="translate(1024,188) rotate(45)">
    <text class="tagline" text-anchor="middle" y="-62">Join</text>
    <text class="tagline" text-anchor="middle" y="-16">the industry and</text>
    <text class="tagline" text-anchor="middle" y="30">train with</text>
    <text class="tagline" text-anchor="middle" y="76">YOUR NAME</text>
  </g>

  <!-- logo -->
  <text class="logo-name" x="114" y="149">Logo Here</text>

  <!-- small accent triangle -->
  <polygon class="accent-triangle" points="2,801 129,705 222,801" fill="var(--cream)"/>

  <!-- bottom bands -->
  <polygon class="headline-band" points="0,804 865,804 642,1025 0,1025" fill="var(--gold)"/>
  <polygon class="mist-band" points="704,969 1199,969 1199,1025 648,1025" fill="var(--mist)"/>
  <polygon class="booking-panel" points="923,746 1199,746 1199,927 1170,966 704,966" fill="var(--plum)"/>
  <polygon class="contact-panel" points="0,1025 642,1025 472,1199 0,1199" fill="var(--cream)"/>

  <!-- headline -->
  <text class="intro" x="110" y="864">Introducing</text>
  <text class="headline" x="60" y="929">Beauty Therapy</text>
  <text class="subhead" x="60" y="983">Route to Aesthetics Training courses</text>

  <!-- booking -->
  <text class="booking" x="1004" y="855" text-anchor="middle">Now Taking</text>
  <text class="booking" x="1004" y="902" text-anchor="middle">Course Bookings</text>

  <!-- contact -->
  <text class="info-label" x="69" y="1084">For Further information</text>
  <text class="phone" x="64" y="1140">call: 1234567890</text>
  <text class="email" x="677" y="1105">email: youremail@mailbox.com</text>
</svg>
</body>
</html>
```